New residential property management company

I have a lot of name recognition in our smaller town due to owning a construction company here. I have now started a residential property management company representing landlords and tenants. Just trying to get my name out there and get some rentals to manage!

```html
<!DOCTYPE html>
<html lang="en">
<head>
<meta charset="utf-8">
<title>Halden Property Management – Flyer</title>
<link href="https://fonts.googleapis.com/css2?family=Montserrat:wght@500;600;800&display=swap" rel="stylesheet">
<style>
  :root {
    --stage: #7d7d7d;
    --ink: #1c1c1e;
    --paper: #f4f4f4;
    --white: #ffffff;
    --navy-deep: #0f1a2c;
    --navy-mid: #24344f;
    --navy-soft: #3c4d68;
  }
  * { box-sizing: border-box; margin: 0; padding: 0; }
  html, body {
    width: 1200px; height: 900px; overflow: hidden;
    background: var(--stage);
    font-family: "Montserrat", Arial, sans-serif;
  }
  .flyer {
    position: absolute; left: 75px; top: 100px;
    width: 1050px; height: 700px;
    display: flex; background: var(--ink);
  }
  .info-column {
    position: relative; width: 470px; height: 100%;
    background: var(--ink); display: flex; flex-direction: column;
  }
  .brand {
    height: 150px; flex: none; background: var(--paper);
    display: flex; align-items: center; gap: 18px; padding: 0 40px;
  }
  .brand-mark { width: 58px; height: 58px; background: var(--ink); flex: none; }
  .brand-name { color: var(--ink); font-weight: 500; line-height: 1; }
  .brand-name .word { display: block; font-size: 60px; letter-spacing: 1px; }
  .brand-name .sub { display: block; font-size: 11px; letter-spacing: 3.2px; margin-top: 6px; }
  .headline {
    height: 118px; flex: none; padding: 22px 30px 0 40px;
    color: var(--white); font-weight: 800; font-size: 32px; line-height: 1.1;
    text-transform: uppercase; white-space: nowrap;
  }
  .content {
    margin-left: 40px; background: var(--paper); flex: none;
    padding: 24px 26px 18px 22px; height: 330px; color: var(--ink);
  }
  .intro { font-size: 13.2px; font-weight: 500; line-height: 1.38; text-align: justify; }
  .services-title { margin-top: 20px; font-size: 19px; font-weight: 800; text-transform: uppercase; }
  .services { list-style: none; margin-top: 6px; }
  .services li {
    display: flex; align-items: center; gap: 8px;
    font-size: 13.5px; font-weight: 500; line-height: 1.72;
  }
  .tick { width: 12px; height: 12px; flex: none; }
  .cta { margin-top: 14px; font-size: 14.5px; font-weight: 800; text-transform: uppercase; }
  .contacts { padding: 20px 0 0 56px; color: var(--white); }
  .contacts p { display: flex; align-items: center; gap: 10px; font-size: 17px; font-weight: 500; line-height: 1.6; }
  .contact-icon { width: 20px; height: 20px; flex: none; }
  .divider {
    width: 26px; height: 100%; background: var(--ink);
    display: flex; justify-content: center;
  }
  .divider::before { content: ""; width: 4px; height: 100%; background: var(--white); }
  .hero-photo {
    flex: 1; height: 100%;
    background:
      radial-gradient(ellipse at 55% 55%, var(--navy-soft) 0%, transparent 55%),
      linear-gradient(160deg, var(--navy-mid) 0%, var(--navy-deep) 70%);
  }
</style>
</head>
<body>
  <main class="flyer">
    <section class="info-column">
      <header class="brand">
        <span class="brand-mark"></span>
        <div class="brand-name">
          <span class="word">HALDEN</span>
          <span class="sub">PROPERTY MANAGEMENT LLC.</span>
        </div>
      </header>

      <h1 class="headline">The Housing Market<br>Is Booming</h1>

      <div class="content">
        <p class="intro">We are a virtual management company with over 14 years experience in title and escrow business. We have a combined 30+ years in management. Our goal is to help other entrepreneurs ease their work load so they can focus on why they got into the business to begin with.</p>

        <h2 class="services-title">Our Services</h2>
        <ul class="services">
          <li><svg class="tick" viewBox="0 0 12 12"><circle cx="6" cy="6" r="6" fill="#1c1c1e"/><path d="M3.2 6.2l1.8 1.8 3.8-3.8" stroke="#fff" stroke-width="1.5" fill="none"/></svg>Take photos and post poctures of listings</li>
          <li><svg class="tick" viewBox="0 0 12 12"><circle cx="6" cy="6" r="6" fill="#1c1c1e"/><path d="M3.2 6.2l1.8 1.8 3.8-3.8" stroke="#fff" stroke-width="1.5" fill="none"/></svg>Post daily content to engage target market</li>
          <li><svg class="tick" viewBox="0 0 12 12"><circle cx="6" cy="6" r="6" fill="#1c1c1e"/><path d="M3.2 6.2l1.8 1.8 3.8-3.8" stroke="#fff" stroke-width="1.5" fill="none"/></svg>Reply to potential buyers and sellers via social media</li>
          <li><svg class="tick" viewBox="0 0 12 12"><circle cx="6" cy="6" r="6" fill="#1c1c1e"/><path d="M3.2 6.2l1.8 1.8 3.8-3.8" stroke="#fff" stroke-width="1.5" fill="none"/></svg>Hashtag research</li>
          <li><svg class="tick" viewBox="0 0 12 12"><circle cx="6" cy="6" r="6" fill="#1c1c1e"/><path d="M3.2 6.2l1.8 1.8 3.8-3.8" stroke="#fff" stroke-width="1.5" fill="none"/></svg>Need something elsa? Just ask!</li>
        </ul>

        <p class="cta">For free consultation call:</p>
      </div>

      <footer class="contacts">
        <p>
          <svg class="contact-icon" viewBox="0 0 20 20"><circle cx="10" cy="10" r="10" fill="#fff"/><path d="M7 5.5l1.6 2.2-1 1.2a6 6 0 0 0 3.5 3.5l1.2-1 2.2 1.6-.9 1.8c-3.8-.2-7.4-3.8-7.6-7.6z" fill="#1c1c1e"/></svg>
          541-555-0187
        </p>
        <p>
          <svg class="contact-icon" viewBox="0 0 20 20"><circle cx="10" cy="10" r="10" fill="#fff"/><rect x="5" y="6.5" width="10" height="7" fill="none" stroke="#1c1c1e" stroke-width="1.4"/><path d="M5 6.8l5 3.8 5-3.8" fill="none" stroke="#1c1c1e" stroke-width="1.4"/></svg>
          haldenpropertymanagement@mail.com
        </p>
      </footer>
    </section>

    <div class="divider"></div>

    <div class="hero-photo" role="img" aria-label="Photo of a man in a dark suit holding out cupped hands beneath a glowing white house outline"></div>
  </main>
</body>
</html>
```